Hotel Loyalty Program Mailer for Halvern Perks Members

I need a postcard mailer that will be sent to prior guests of our hotel.

This postcard would invite them to stay at our hotel and receive 3,000 Bonus Halvern points. The terms of the mailer would be that they must bring card at check in to receive the bonus points.

The purpose of this mailer would be to get the word out about our new fully renovated rooms, our restaurant that has a brand new menu and management team.

This card would highlight all of the very exciting changes that are happening here as we become a new hotel brand "Quill by Halvern"

The room photos are too big to attach they can be pullet from

www.halvern-stays.example/tqbox

Target Market(s)

Halvern Perk members that have stayed at our property in the past.

Industry/Entity Type

Hotel

Font styles to use
Other font styles liked:
• courier

Colors
3176b5
0355a3
85abd2
85cae6

Requirements
Must have
• Must be modern design. Include room pictures halvern perk logo quill logo and dunmore architect logo. We are renovating our hotel to become a Quill by Halvern and are STILL a halvern hotel. Members receive points when they stay. With this card they will receive 3,000 bonus points on their next stay. Must highlight the new rooms and new menu /management in the resturant Should include our address phone number and website
Should not have
• Any pictures of the hotel EXCEPT the room pictures on our website. www.halvern-stays.example/tqbox

```html
<!DOCTYPE html>
<html lang="en">
<head>
<meta charset="utf-8">
<title>Dunmore Architect – Halvern Perks Postcard Mailer</title>
<link rel="stylesheet" href="https://fonts.googleapis.com/css2?family=Anton&family=Archivo+Narrow:wght@500;600&family=PT+Sans:wght@400;700&display=swap">
<style>
  :root {
    --stage: #e9e7e4;
    --navy: #0b3a86;
    --brand-blue: #0355a3;
    --mid-blue: #3176b5;
    --soft-blue: #85abd2;
    --sky: #85cae6;
    --panel-sky: #7dc4ec;
    --ink: #111111;
    --paper: #ffffff;
    --rule: #b9b9b9;
    --room-wall: #7a6550;
    --room-linen: #e9e6e0;
  }
  * { box-sizing: border-box; margin: 0; padding: 0; }
  html, body { width: 1200px; height: 1000px; overflow: hidden; }
  body { background: var(--stage); position: relative; font-family: "PT Sans", Arial, sans-serif; }

  .postcard { position: absolute; background: var(--paper); box-shadow: 0 2px 8px rgba(0,0,0,.18); }
  .postcard--front { left: 47px; top: 37px; width: 583px; height: 451px; overflow: hidden; }
  .postcard--back { left: 547px; top: 505px; width: 584px; height: 453px; }

  .room-photo { position: absolute; background: linear-gradient(180deg, var(--room-wall) 0%, #8d7660 45%, var(--room-linen) 62%, #f6f4f0 100%); }
  .room-photo--top-left { left: 0; top: 0; width: 293px; height: 221px; }
  .room-photo--top-right { left: 298px; top: 0; width: 285px; height: 228px; }
  .room-photo--bottom-left { left: 0; top: 225px; width: 293px; height: 226px; }

  .offer-panel { position: absolute; left: 298px; top: 228px; width: 285px; height: 223px; background: var(--panel-sky); color: var(--navy); }
  .offer-panel__lead { position: absolute; left: 90px; top: 5px; font-size: 9px; font-weight: 700; letter-spacing: .1px; }
  .offer-panel__points { position: absolute; left: 60px; width: 180px; top: 15px; text-align: center; font-size: 40px; font-weight: 700; line-height: 1; }
  .offer-panel__unit { position: absolute; left: 60px; width: 180px; top: 61px; text-align: center; font-size: 12px; font-weight: 700; }
  .offer-panel__terms { position: absolute; left: 60px; top: 77px; width: 174px; height: 9px; background: var(--ink); color: var(--paper); font-size: 5.6px; line-height: 9px; text-align: center; letter-spacing: .1px; white-space: nowrap; overflow: hidden; }
  .feature-list { position: absolute; left: 18px; top: 100px; list-style: none; font-size: 14px; font-weight: 700; line-height: 15px; }
  .feature-list li { display: flex; gap: 6px; margin-bottom: 9px; }
  .feature-list li:nth-child(2) { padding-left: 22px; text-align: center; }
  .tick-box { flex: none; width: 9px; height: 9px; margin-top: 3px; }
  .partner-badge { position: absolute; top: 168px; height: 34px; background: var(--navy); border: 1px solid var(--paper); }
  .partner-badge--perks { left: 66px; width: 67px; }
  .partner-badge--quill { left: 149px; width: 34px; }

  .identity-hex { position: absolute; left: 200px; top: 123px; width: 178px; height: 205px; }
  .identity-hex__content { position: absolute; inset: 0; text-align: center; color: var(--ink); }
  .brand-dot { display: block; margin: 38px auto 0; width: 26px; height: 26px; border-radius: 50%; background: var(--brand-blue); }
  .brand-name { font-family: "Archivo Narrow", Arial, sans-serif; font-weight: 600; color: var(--brand-blue); font-size: 15px; letter-spacing: .2px; margin-top: 9px; line-height: 1; white-space: nowrap; }
  .brand-tagline { font-size: 5.5px; letter-spacing: 1px; color: var(--brand-blue); margin-top: 2px; white-space: nowrap; }
  .identity-hex__address { font-size: 9px; line-height: 13px; margin-top: 6px; }
  .identity-hex__web { font-size: 9px; font-weight: 700; color: var(--navy); }

  .lunch-panel { position: absolute; left: 0; top: 0; width: 286px; height: 368px; background: #0a0a0a; border-right: 3px solid var(--brand-blue); border-bottom: 3px solid var(--brand-blue); border-bottom-right-radius: 22px; overflow: hidden; color: var(--paper); text-align: center; }
  .news-line { font-size: 15px; font-weight: 700; line-height: 1; }
  .news-line--first { margin-top: 36px; }
  .news-line--second { margin-top: 6px; }
  .news-line span.new { color: var(--sky); }
  .news-line .pip { display: inline-block; width: 5px; height: 5px; background: var(--sky); vertical-align: middle; margin: 0 4px 3px 0; }
  .news-line .gap { display: inline-block; width: 18px; }
  .lunch-panel__blurb { font-size: 7.5px; line-height: 10px; margin-top: 17px; }
  .lunch-panel__headline { position: relative; z-index: 1; font-family: "Anton", Impact, sans-serif; font-size: 25px; line-height: 1.1; letter-spacing: .3px; margin-top: 10px; color: var(--navy); -webkit-text-stroke: 1px var(--paper); }
  .dish-photo { position: absolute; left: 0; top: 160px; width: 283px; height: 205px; background: radial-gradient(ellipse at 45% 55%, #8a8a8a 0%, #4a4a4a 30%, #1a1a1a 70%, #0a0a0a 100%); }

  .return-address { position: absolute; left: 290px; top: 30px; width: 140px; text-align: center; color: var(--ink); }
  .return-address .brand-dot { margin-top: 0; width: 22px; height: 22px; }
  .return-address .brand-name { font-size: 13px; margin-top: 5px; }
  .return-address__lines { font-size: 8.5px; line-height: 10px; margin-top: 6px; }
  .stamp-box { position: absolute; left: 461px; top: 28px; width: 92px; height: 92px; border: 1px solid var(--rule); }
  .address-rule { position: absolute; left: 318px; width: 235px; height: 1px; background: var(--rule); }
</style>
</head>
<body>

<section class="postcard postcard--front" aria-label="Postcard front">
  <div class="room-photo room-photo--top-left" role="img" aria-label="Photo of a renovated guest room with a king bed and lamps"></div>
  <div class="room-photo room-photo--top-right" role="img" aria-label="Photo of a renovated guest room with two queen beds"></div>
  <div class="room-photo room-photo--bottom-left" role="img" aria-label="Photo of a renovated guest room with bed and armchair"></div>

  <div class="offer-panel">
    <p class="offer-panel__lead">STAY AT OUR HOTEL AND RECEIVE</p>
    <p class="offer-panel__points">3,000</p>
    <p class="offer-panel__unit">BONUS HALVERN POINTS</p>
    <p class="offer-panel__terms">BRING THE CARD AT CHECK IN TO RECEIVE THE BONUS POINTS</p>
    <ul class="feature-list">
      <li><svg class="tick-box" viewBox="0 0 10 10"><rect x=".5" y=".5" width="9" height="9" fill="none" stroke="#0b3a86"/><path d="M2 5l2 2 4-4" fill="none" stroke="#0b3a86" stroke-width="1.6"/></svg>NEW FULLY RENOVATED ROOMS</li>
      <li><svg class="tick-box" viewBox="0 0 10 10"><rect x=".5" y=".5" width="9" height="9" fill="none" stroke="#0b3a86"/><path d="M2 5l2 2 4-4" fill="none" stroke="#0b3a86" stroke-width="1.6"/></svg><span>BRAND NEW MENU AND<br>MANAGEMENT TEAM.</span></li>
    </ul>
    <div class="partner-badge partner-badge--perks" role="img" aria-label="Halvern Perks badge"></div>
    <div class="partner-badge partner-badge--quill" role="img" aria-label="Quill by Halvern badge"></div>
  </div>

  <div class="identity-hex">
    <svg width="178" height="205" viewBox="0 0 178 205" aria-hidden="true">
      <defs>
        <linearGradient id="hexFill" x1="0" y1="0" x2="1" y2="1">
          <stop offset="0" stop-color="#ffffff"/><stop offset="1" stop-color="#e6e8ec"/>
        </linearGradient>
      </defs>
      <polygon points="89,3 175,47 175,158 89,202 3,158 3,47" fill="url(#hexFill)" stroke="#0b3a86" stroke-width="5"/>
    </svg>
    <div class="identity-hex__content">
      <span class="brand-dot"></span>
      <p class="brand-name">DUNMORE ARCHITECT</p>
      <p class="brand-tagline">HOTEL &amp; CONFERENCE CENTER</p>
      <p class="identity-hex__address">4820 Linden Avenue Hwy 9<br>Fairholt Wisconsin 53990 USA<br>+1-555-014-2290</p>
      <p class="identity-hex__web">www.halvern-stays.example/tqbox</p>
    </div>
  </div>
</section>

<section class="postcard postcard--back" aria-label="Postcard back">
  <div class="lunch-panel">
    <div class="dish-photo" role="img" aria-label="Black and white photo of a burger on a plate"></div>
    <p class="news-line news-line--first"><i class="pip"></i><span class="new">NEW</span> MENU<i class="gap"></i><i class="pip"></i><span class="new">NEW</span> HOURS</p>
    <p class="news-line news-line--second"><i class="pip"></i><span class="new">NEW</span> MANAGEMENT</p>
    <p class="lunch-panel__blurb">featuring fresh ingredients, friendly service, and<br>a relaxing atmosphere</p>
    <p class="lunch-panel__headline">JOIN US FOR LUNCH</p>
  </div>

  <div class="return-address">
    <span class="brand-dot"></span>
    <p class="brand-name">DUNMORE ARCHITECT</p>
    <p class="brand-tagline">HOTEL &amp; CONFERENCE CENTER</p>
    <p class="return-address__lines">4820 Linden Avenue<br>Hwy 9 Fairholt<br>Wisconsin 53990 USA<br>+1-555-014-2290</p>
  </div>
  <div class="stamp-box" aria-label="Stamp area"></div>
  <div class="address-rule" style="top:201px"></div>
  <div class="address-rule" style="top:263px"></div>
  <div class="address-rule" style="top:325px"></div>
</section>

</body>
</html>
```